Industrial Automation company requires a business card design

Valtrin Automation provides design & build of Automated Equipment for manufacturing industry.
www.valtrinautomation.example
The equipment we design is used for manufacturing in sectors such as medical device, pharmaceutical, aerospace and electronics.
We require a new business card design which incorporates our (New) logo and the key message words:
Automated Equipment:
Design, Build, Control, Test, Support

```html
<!DOCTYPE html>
<html lang="en">
<head>
<meta charset="utf-8">
<title>Valtrin Automation – Business Card</title>
<link href="https://fonts.googleapis.com/css2?family=Lato:wght@400;700&display=swap" rel="stylesheet">
<style>
  :root {
    --stage: #3a3a3a;
    --paper: #f4f4f4;
    --ink: #1d1d1d;
    --black-panel: #151515;
    --brand-green: #0a7a36;
    --card-green: #05713a;
    --white: #ffffff;
  }
  * { box-sizing: border-box; margin: 0; padding: 0; }
  html, body { width: 1200px; height: 929px; overflow: hidden; }
  body {
    background: var(--stage);
    font-family: "Lato", sans-serif;
    position: relative;
  }
  .card {
    position: absolute;
    left: 341px;
    width: 518px;
    height: 297px;
    border-radius: 8px;
    overflow: hidden;
  }
  .card--front { top: 126px; background: var(--paper); }
  .card--back { top: 457px; height: 295px; background: var(--card-green); }

  .front-panel { position: absolute; inset: 0; width: 100%; height: 100%; }

  .brand {
    display: flex;
    align-items: center;
    gap: 10px;
    font-weight: 700;
    white-space: nowrap;
  }
  .brand__dot { border-radius: 50%; flex: none; }
  .card--front .brand {
    position: absolute;
    left: 24px;
    top: 44px;
    font-size: 28px;
    color: var(--brand-green);
  }
  .card--front .brand__dot { width: 22px; height: 22px; background: var(--brand-green); }

  .person { position: absolute; left: 23px; top: 122px; }
  .person__name { font-size: 22px; font-weight: 700; color: var(--brand-green); line-height: 1.1; }
  .person__role { font-size: 14px; color: var(--ink); margin-top: 2px; }

  .contact {
    position: absolute;
    left: 22px;
    top: 182px;
    font-size: 14.5px;
    color: var(--ink);
    line-height: 18px;
    list-style: none;
  }
  .contact__address { margin-bottom: 2px; }
  .contact__item { display: flex; align-items: center; gap: 6px; }
  .contact__item svg { width: 13px; height: 13px; flex: none; }

  .card--back .brand {
    position: absolute;
    left: 0; right: 0;
    top: 122px;
    justify-content: center;
    font-size: 34px;
    color: var(--white);
  }
  .card--back .brand__dot { width: 26px; height: 26px; background: var(--white); }

  .tagline {
    position: absolute;
    left: 0; right: 0;
    top: 259px;
    height: 22px;
    background: var(--white);
    color: var(--ink);
    font-size: 14.5px;
    text-align: center;
    line-height: 22px;
  }
</style>
</head>
<body>
  <section class="card card--front">
    <svg class="front-panel" viewBox="0 0 518 297" preserveAspectRatio="none" aria-hidden="true">
      <path d="M431 0 C495 50 528 150 474 204 C410 262 260 282 139 297 L518 297 L518 0 Z" fill="var(--black-panel)"/>
    </svg>

    <div class="brand"><span class="brand__dot"></span>Valtrin Automation</div>

    <div class="person">
      <p class="person__name">Aidan Rourke</p>
      <p class="person__role">President</p>
    </div>

    <ul class="contact">
      <li class="contact__address">Glenmara, Castlebrook</li>
      <li class="contact__address">Co. Lorne, Ireland</li>
      <li class="contact__item">
        <svg viewBox="0 0 16 16" aria-hidden="true"><path fill="var(--brand-green)" d="M1 6c0-2 3-3 7-3s7 1 7 3v1h-3.5V5.5h-7V7H1z M3 8h10l1.5 5h-13z"/><circle cx="8" cy="10.5" r="1.6" fill="var(--paper)"/></svg>
        +353 (0) 55 01234
      </li>
      <li class="contact__item">
        <svg viewBox="0 0 16 16" aria-hidden="true"><rect x="1" y="3" width="14" height="10" fill="var(--brand-green)"/><path d="M1.5 3.5 8 9l6.5-5.5M1.5 12.5l5-4.5M14.5 12.5l-5-4.5" stroke="var(--paper)" stroke-width="1.1" fill="none"/></svg>
        info@valtrinautomation.example
      </li>
      <li class="contact__item">
        <svg viewBox="0 0 16 16" aria-hidden="true"><circle cx="8" cy="8" r="7" fill="var(--brand-green)"/><g stroke="var(--paper)" stroke-width="0.9" fill="none"><ellipse cx="8" cy="8" rx="3" ry="7"/><path d="M1 8h14M2 4.5h12M2 11.5h12M8 1v14"/></g></svg>
        www.valtrinautomation.example
      </li>
    </ul>
  </section>

  <section class="card card--back">
    <div class="brand"><span class="brand__dot"></span>Valtrin Automation</div>
    <p class="tagline">Automated Equipment: Design, Build, Control, Test, Support</p>
  </section>
</body>
</html>
```